Zerovan Medical

We are a medical supplier company we sell machines and equipment to all medical sectors in Iraq. Our services include not only the installation of these machines and equipment but also we provide support after installation and we train the staff to use these machines/equipment
We need a website that will make us stand out from our competitors, something professional and catchy
Starting from the home page, before showing the home page we want the loading screen to have our logo animated in a nice way
Then we can proceed to creating the other pages which are
Projects
Services
Training
About
and Contact us
Attached below is our logo and the color blue that we hope to use in the theme of the website
**** In the home page we want to focus on our partners and services****

Target Market(s)

Medical Sector

Industry/Entity Type

Medical

Coding

Coded - Design and coding required

Number of Pages Required

5+ page

Colors
0054AA
0677BA
7BADD7
CADEEF
E8F1F8

Requirements
Must have
• Animation in loading screen or animation in home page
Nice to have
• Some sort of animation for our partners

```html
<!DOCTYPE html>
<html lang="en">
<head>
<meta charset="utf-8">
<title>Zerovan Medical – Home</title>
<link href="https://fonts.googleapis.com/css2?family=Exo+2:wght@400;600;700&family=Roboto:wght@400;500;700&display=swap" rel="stylesheet">
<style>
:root{
  --navy:#1f1c5c;
  --navy-deep:#1a1852;
  --blue:#1e9bd7;
  --blue-dark:#0677ba;
  --sky:#cadeef;
  --mist:#e8f1f8;
  --grey-bg:#a3a3a3;
  --text:#555;
  --white:#fff;
}
*{margin:0;padding:0;box-sizing:border-box}
html,body{width:1200px;height:2538px;overflow:hidden;background:var(--grey-bg);font-family:"Roboto",Arial,sans-serif;color:var(--text)}
.stage{position:absolute;left:0;top:0;width:1218px;height:2576px;transform:scale(.9852);transform-origin:0 0}
.page{position:absolute;left:48px;top:70px;width:534px;height:2435px;background:var(--white);overflow:hidden}
.abs{position:absolute}
.h-font{font-family:"Exo 2",Arial,sans-serif}
.sec-title{position:absolute;left:0;width:534px;text-align:center;font-family:"Exo 2",Arial,sans-serif;font-size:17px;color:var(--navy);font-weight:400}
.sec-title b{font-weight:700}
.sec-title::after{content:"";display:block;width:32px;height:2px;background:var(--blue);margin:3px auto 0}
.sec-title.light{color:var(--white)}
.btn{position:absolute;background:var(--blue);color:#fff;font-size:6px;font-weight:700;text-transform:uppercase;display:flex;align-items:center;justify-content:center;gap:3px;letter-spacing:.2px}
.btn i{display:inline-block;width:6px;height:6px;border-radius:50%;background:#fff;position:relative}
.btn i::after{content:"";position:absolute;left:2px;top:1.5px;border-left:2.5px solid var(--blue);border-top:1.5px solid transparent;border-bottom:1.5px solid transparent}
.btn.navy{background:var(--navy)}
.btn.navy i::after{border-left-color:var(--navy)}
.para{position:absolute;font-size:6px;line-height:11.5px;color:#6a6a6a}
.topbar{left:0;top:0;width:534px;height:13px;background:var(--navy);color:#fff;font-size:5.3px;display:flex;justify-content:flex-end;align-items:center;gap:10px;padding-right:50px}
.brand{left:49px;top:16px;display:flex;align-items:center;gap:5px;font-family:"Exo 2",Arial,sans-serif;font-weight:700;font-size:12px;color:var(--navy)}
.brand span.sq{width:18px;height:14px;border:2px solid var(--blue)}
.nav{left:173px;top:24px;display:flex;gap:11px;font-size:6px;font-weight:500;color:var(--navy)}
.nav .on{color:var(--blue)}
.hero-photo{left:0;top:43px;width:534px;height:290px;background:linear-gradient(100deg,#f3f7fb 0%,#dfe8f1 40%,#b8c9da 70%,#dfe7ef 100%)}
.arrow-c{position:absolute;width:15px;height:15px;border-radius:50%;background:#6d7a88;display:flex;align-items:center;justify-content:center}
.arrow-c svg{width:6px;height:6px}
.svc{position:absolute;width:130px;text-align:center}
.svc .ic{width:40px;height:40px;border-radius:50%;background:var(--navy);margin:0 auto;display:flex;align-items:center;justify-content:center}
.svc .ic.blue{background:var(--blue)}
.svc h4{font-size:7px;color:#222;margin-top:10px;font-weight:700}
.svc p{font-size:5.6px;line-height:10px;color:#7a7a7a;margin-top:5px}
.svc a{display:inline-block;margin-top:6px;font-size:6px;font-weight:700;color:var(--navy);text-decoration:underline}
.prod{position:absolute;top:927px;width:100px;height:129px;background:#fff;text-align:center}
.prod .img{width:70px;height:68px;margin:8px auto 0;background:linear-gradient(180deg,#e5ecf3,#a9bccf)}
.prod h5{font-size:6.8px;color:#222;margin-top:9px;font-weight:700}
.prod p{font-size:5.4px;line-height:8.5px;color:#777;margin-top:3px}
.prod .btn{left:21px;top:123px;width:58px;height:13px}
.proj{position:absolute;width:170px;font-size:5.5px;line-height:9.5px;color:#777}
.proj h5{font-size:6.5px;color:#222;font-weight:700;margin-bottom:3px}
.proj.l{text-align:right}
.num{position:absolute;width:24px;height:24px;border-radius:50%;color:#fff;font-size:8px;font-weight:700;display:flex;align-items:center;justify-content:center;border:2px solid #fff;box-shadow:0 0 0 1px #ddd}
.num.b{background:var(--blue)}.num.n{background:var(--navy)}
.partner{position:absolute;top:1778px;width:136px;height:80px;background:#fff;box-shadow:0 2px 6px rgba(0,0,0,.12);text-align:center;padding-top:9px}
.partner h5{font-size:6.5px;color:#222;font-weight:700}
.partner p{font-size:5.6px;line-height:10px;color:#777;margin:5px 10px 0}
.partner a{display:block;margin-top:6px;font-size:5.8px;font-weight:700;color:var(--blue)}
.partner-name{position:absolute;top:1874px;width:136px;display:flex;justify-content:center;align-items:center;gap:4px;font-size:7px;font-weight:700;color:var(--navy);letter-spacing:.5px}
.partner-name i{width:7px;height:7px;border-radius:50%;background:var(--blue)}
.field{position:absolute;width:102px;font-size:5.8px}
.field b{display:block;color:#222;font-weight:700;font-size:6px}
.field span{display:block;color:#999;font-size:5px;margin-top:6px;padding-bottom:5px;border-bottom:1px solid #ddd}
.foot{color:#fff;font-size:5.8px}
.foot h6{font-size:7.5px;font-weight:700;margin-bottom:12px}
.foot li{list-style:none;line-height:12px}
.foot .ci{display:flex;gap:8px;margin-bottom:7px;line-height:8px}
.foot .ci i{width:5px;height:5px;background:var(--blue);border-radius:1px;margin-top:1px;flex:none}
.loader{position:absolute;left:637px;top:70px;width:533px;height:286px;background:var(--navy-deep);display:flex;align-items:center;justify-content:center;gap:10px}
.loader .sq{width:20px;height:20px;border:3px solid var(--blue)}
.loader b{font-family:"Exo 2",Arial,sans-serif;font-size:30px;font-weight:700;color:#fff}
</style>
</head>
<body>
<div class="stage">

<main class="page">
  <div class="abs topbar"><span>☎ (555) 010 0100</span><span>|</span><span>✉ info@zerovan.com</span><span>|</span><span>◷ Mon - Sun: 9.00am to 9 pm</span></div>
  <div class="abs brand"><span class="sq"></span>Zerovan</div>
  <nav class="abs nav"><span class="on">Home</span><span>Projects</span><span>Services</span><span>Training</span><span>About</span><span>Contact us</span><span>EN ▾</span></nav>
  <div class="btn" style="left:429px;top:19px;width:56px;height:17px;font-size:6px;text-transform:none;font-weight:500">Get in Touch</div>

  <div class="abs hero-photo" role="img" aria-label="Photo of a medical ventilator in a bright hospital room"></div>
  <h1 class="abs h-font" style="left:50px;top:114px;font-size:28px;color:var(--navy);font-weight:700">Zerovan</h1>
  <p class="abs" style="left:50px;top:154px;width:200px;font-size:6.4px;line-height:11px;color:#222">Lorem ipsum dolor sit amet, consectetur adipiscing elit, incididunt ut labore et dolore magna aliqua.</p>
  <div class="btn" style="left:50px;top:190px;width:83px;height:20px;font-size:6.5px">Get Started <i></i></div>
  <div class="arrow-c" style="left:16px;top:152px"><svg viewBox="0 0 6 6"><path d="M4 0.5 1.5 3 4 5.5" stroke="#fff" fill="none"/></svg></div>
  <div class="arrow-c" style="left:503px;top:152px"><svg viewBox="0 0 6 6"><path d="M2 0.5 4.5 3 2 5.5" stroke="#fff" fill="none"/></svg></div>
  <svg class="abs" style="left:0;top:280px" width="534" height="60" viewBox="0 0 534 60">
    <path d="M0 30 C120 60 300 0 534 28 L534 60 0 60Z" fill="#fff"/>
    <path d="M0 25 C150 52 260 2 420 8 C470 10 510 20 534 30 L534 36 C500 24 460 16 420 16 C270 14 150 56 0 32Z" fill="var(--navy)"/>
    <path d="M330 15 C420 0 490 12 534 25 L534 30 C490 18 420 8 330 18Z" fill="var(--blue)"/>
  </svg>

  <div class="abs" role="img" aria-label="Large panel filled with a blue medical equipment photo" style="left:50px;top:362px;width:200px;height:153px;background:linear-gradient(135deg,#cfe3f2,#5ea6d3 55%,#2f86c3)"></div>
  <h2 class="abs h-font" style="left:285px;top:360px;font-size:17px;color:var(--navy);font-weight:400"><b style="font-weight:700">About</b> Us</h2>
  <div class="abs" style="left:285px;top:381px;width:32px;height:2px;background:var(--blue)"></div>
  <p class="para" style="left:285px;top:393px;width:202px">Lorem ipsum dolor sit amet, consectetur adipiscing elit, sed do eiusmod tempor incididunt ut labore et dolore magna aliqua. Ut enim ad minim veniam, quis nostrud exercitation ullamco laboris nisi ut aliquip ex ea commodo consequat.</p>
  <p class="para" style="left:285px;top:445px;width:202px">Sed ut perspiciatis unde omnis iste natus error sit voluptatem accusantium doloremque laudantium, totam rem aperiam, eaque ipsa quae ab illo quasi beatae vitae dicta sunt explicabo.</p>
  <div class="btn" style="left:285px;top:492px;width:78px;height:20px">Learn More <i></i></div>

  <svg class="abs" style="left:0;top:530px" width="534" height="330" viewBox="0 0 534 330">
    <defs><linearGradient id="svcbg" x1="0" y1="0" x2="0" y2="1"><stop offset="0" stop-color="#eef4fa"/><stop offset="1" stop-color="#e3edf6"/></linearGradient></defs>
    <path d="M0 10 C90 60 190 40 320 20 C420 5 490 5 534 15 L534 290 C460 250 360 270 260 300 C150 330 60 300 0 270Z" fill="url(#svcbg)"/>
  </svg>
  <h2 class="sec-title" style="top:593px"><b>Our</b> Services</h2>
  <div class="abs" style="left:197px;top:635px;width:140px;height:147px;background:#fff;border-radius:28px 0 28px 0;box-shadow:0 3px 10px rgba(0,0,0,.1)"></div>
  <div class="svc" style="left:54px;top:648px">
    <div class="ic"><svg width="20" height="20" viewBox="0 0 20 20" stroke="#fff" stroke-width="1.5" fill="none"><path d="M4 4 16 16M16 4 4 16"/></svg></div>
    <h4>Installation</h4><p>Sed ut perspiciatis unde omnis iste natus sit voluptatem accusantium doloremque laudantium, totam rem aperiam, eaque ipsa quae ab illo inventore</p><a>READ MORE ➜</a></div>
  <div class="svc" style="left:202px;top:648px">
    <div class="ic blue"><svg width="20" height="20" viewBox="0 0 20 20" stroke="#fff" stroke-width="1.5" fill="none"><circle cx="10" cy="6" r="3"/><path d="M4 17c0-4 3-6 6-6s6 2 6 6"/></svg></div>
    <h4>We Train The Staff</h4><p>Sed ut perspiciatis unde omnis iste natus sit voluptatem accusantium doloremque laudantium, totam rem aperiam, eaque ipsa quae ab illo inventore</p><a style="color:var(--blue)">READ MORE ➜</a></div>
  <div class="svc" style="left:349px;top:648px">
    <div class="ic"><svg width="20" height="20" viewBox="0 0 20 20" stroke="#fff" stroke-width="1.5" fill="none"><rect x="4" y="3" width="12" height="9"/><path d="M10 12v5M6 17h8"/></svg></div>
    <h4>Medical Supplier</h4><p>Sed ut perspiciatis unde omnis iste natus sit voluptatem accusantium doloremque laudantium, totam rem aperiam, eaque ipsa quae ab illo inventore</p><a>READ MORE ➜</a></div>

  <svg class="abs" style="left:0;top:800px" width="534" height="350" viewBox="0 0 534 350">
    <path d="M0 40 C90 70 200 45 300 20 C400 -5 480 5 534 35 L534 300 C450 265 330 280 220 310 C120 340 40 325 0 300Z" fill="var(--navy)"/>
    <path d="M420 8 C470 6 510 20 534 35 L534 40 C505 24 470 14 420 12Z" fill="var(--blue)"/>
    <path d="M420 270 C470 268 510 285 534 300 L534 306 C505 290 470 278 420 274Z" fill="var(--blue)"/>
  </svg>
  <h2 class="sec-title light" style="top:854px"><b>Our</b> Products</h2>
  <p class="abs" style="left:108px;top:888px;width:318px;text-align:center;font-size:5.8px;line-height:10.5px;color:#fff">Lorem ipsum dolor sit amet, consectetur adipiscing elit, sed do eiusmod tempor incididunt ut labore et dolore magna quis nostrud exercitation ullamco laboris nisi ut aliquip aliqua.</p>
  <div class="prod" style="left:50px"><div class="img" role="img" aria-label="Anesthesia workstation product photo"></div><h5>Product Name</h5><p>Lorem ipsum dolor sit amet,<br>consectetur elit,</p><div class="btn">Learn More <i></i></div></div>
  <div class="prod" style="left:162px"><div class="img" role="img" aria-label="Patient monitor cart product photo"></div><h5>Product Name</h5><p>Lorem ipsum dolor sit amet,<br>consectetur elit,</p><div class="btn">Learn More <i></i></div></div>
  <div class="prod" style="left:273px"><div class="img" role="img" aria-label="Ventilator product photo"></div><h5>Product Name</h5><p>Lorem ipsum dolor sit amet,<br>consectetur elit,</p><div class="btn">Learn More <i></i></div></div>
  <div class="prod" style="left:384px"><div class="img" role="img" aria-label="Ultrasound system product photo"></div><h5>Product Name</h5><p>Lorem ipsum dolor sit amet,<br>consectetur elit,</p><div class="btn">Learn More <i></i></div></div>
  <svg class="abs" style="left:18px;top:983px" width="10" height="18" viewBox="0 0 10 18"><path d="M8 1 2 9 8 17" stroke="#fff" stroke-width="2" fill="none"/></svg>
  <svg class="abs" style="left:506px;top:983px" width="10" height="18" viewBox="0 0 10 18"><path d="M2 1 8 9 2 17" stroke="#fff" stroke-width="2" fill="none"/></svg>

  <h2 class="sec-title" style="top:1166px"><b>Our</b> Projects</h2>
  <div class="abs" style="left:237px;top:1237px;height:148px;border-left:1px dashed var(--navy)"></div>
  <div class="abs" style="left:296px;top:1237px;height:148px;border-left:1px dashed var(--navy)"></div>
  <div class="abs" style="left:257px;top:1300px;width:16px;height:14px;border:2px solid var(--blue)"></div>
  <div class="num b" style="left:225px;top:1213px">01</div>
  <div class="num n" style="left:225px;top:1268px">02</div>
  <div class="num b" style="left:225px;top:1323px">03</div>
  <div class="num n" style="left:225px;top:1378px">04</div>
  <div class="num n" style="left:284px;top:1213px">05</div>
  <div class="num b" style="left:284px;top:1268px">06</div>
  <div class="num n" style="left:284px;top:1323px">07</div>
  <div class="num b" style="left:284px;top:1378px">08</div>
  <div class="proj l" style="left:43px;top:1210px"><h5>Medora State Co.</h5>Lorem ipsum dolor sit amet, consectetur adipiscing incididunt ut et dolore magna aliqua.</div>
  <div class="proj l" style="left:43px;top:1265px"><h5>Northbay Health Office</h5>Lorem ipsum dolor sit amet, consectetur adipiscing incididunt ut et dolore magna aliqua.</div>
  <div class="proj l" style="left:43px;top:1320px"><h5>Westgate Department of Health</h5>Lorem ipsum dolor sit amet, consectetur adipiscing incididunt ut et dolore magna aliqua.</div>
  <div class="proj l" style="left:43px;top:1375px"><h5>Northbay Health Office</h5>Lorem ipsum dolor sit amet, consectetur adipiscing incididunt ut et dolore magna aliqua.</div>
  <div class="proj" style="left:320px;top:1210px"><h5>Northbay Health Office</h5>Lorem ipsum dolor sit amet, consectetur adipiscing incididunt ut et dolore magna aliqua.</div>
  <div class="proj" style="left:320px;top:1265px"><h5>Ashford Hospital in Eastvale province</h5>Lorem ipsum dolor sit amet, consectetur adipiscing incididunt ut et dolore magna aliqua.</div>
  <div class="proj" style="left:320px;top:1320px"><h5>Burn Center Hospital in Riverside city</h5>Lorem ipsum dolor sit amet, consectetur adipiscing incididunt ut et dolore magna aliqua.</div>
  <div class="proj" style="left:320px;top:1375px"><h5>Corvain Hospital turn key project</h5>Lorem ipsum dolor sit amet, consectetur adipiscing incididunt ut et dolore magna aliqua.</div>

  <svg class="abs" style="left:0;top:1430px" width="534" height="290" viewBox="0 0 534 290">
    <path d="M0 10 C100 50 230 45 340 20 C430 0 500 0 534 15 L534 280 C470 230 380 235 280 255 C170 280 60 285 0 255Z" fill="var(--blue)"/>
    <path d="M0 8 C100 45 230 40 340 16 C260 38 120 48 0 14Z" fill="var(--navy)"/>
    <path d="M400 232 C460 225 505 250 534 275 L534 282 C505 258 460 234 400 236Z" fill="var(--navy)"/>
  </svg>
  <h2 class="abs h-font" style="left:50px;top:1505px;font-size:17px;color:#fff;font-weight:700">Training</h2>
  <div class="abs" style="left:50px;top:1529px;width:32px;height:2px;background:var(--navy)"></div>
  <p class="para" style="left:50px;top:1540px;width:208px;color:#fff">Lorem ipsum dolor sit amet, consectetur adipiscing elit, sed do eiusmod tempor incididunt ut labore et dolore magna aliqua. Ut enim ad minim veniam, quis nostrud exercitation ullamco laboris nisi ut aliquip ex ea commodo consequat.</p>
  <p class="para" style="left:50px;top:1592px;width:208px;color:#fff">Sed ut perspiciatis unde omnis iste natus error sit voluptatem accusantium doloremque laudantium, totam rem aperiam, eaque ipsa quae ab illo quasi beatae vitae dicta sunt explicabo.</p>
  <div class="btn navy" style="left:50px;top:1641px;width:78px;height:20px">Learn More <i></i></div>
  <div class="abs" role="img" aria-label="Photo of a technician working at a laboratory machine" style="left:297px;top:1466px;width:184px;height:184px;border-radius:50%;border:4px solid #fff;background:linear-gradient(135deg,#dbe6f0,#7fa3c4 50%,#2f5878)"></div>

  <h2 class="sec-title" style="top:1733px"><b>Our</b> Partners</h2>
  <div class="partner" style="left:50px"><h5>HALVERN MEDTEC</h5><p>Sed ut perspiciatis unde omnis iste natus error sit voluptatem accusantium quasi dicta sunt explicabo.</p><a>LEARN MORE ➜</a></div>
  <div class="partner" style="left:199px;border-bottom:2px solid var(--navy)"><h5>ORIVEL GLOBAL</h5><p>Sed ut perspiciatis unde omnis iste natus error sit voluptatem accusantium quasi dicta sunt explicabo.</p><a>LEARN MORE ➜</a></div>
  <div class="partner" style="left:347px"><h5>KESTRAN</h5><p>Sed ut perspiciatis unde omnis iste natus error sit voluptatem accusantium quasi dicta sunt explicabo.</p><a>LEARN MORE ➜</a></div>
  <div class="partner-name" style="left:50px"><i></i>HALVERN</div>
  <div class="partner-name" style="left:199px"><i></i>ORIVEL</div>
  <div class="partner-name" style="left:347px"><i></i>KESTRAN</div>
  <svg class="abs" style="left:19px;top:1812px" width="8" height="14" viewBox="0 0 8 14"><path d="M7 1 1 7 7 13" stroke="#999" stroke-width="1.5" fill="none"/></svg>
  <svg class="abs" style="left:507px;top:1812px" width="8" height="14" viewBox="0 0 8 14"><path d="M1 1 7 7 1 13" stroke="#999" stroke-width="1.5" fill="none"/></svg>
  <div class="btn" style="left:224px;top:1911px;width:86px;height:18px">View All Partners <i></i></div>

  <div class="abs" style="left:49px;top:1975px;width:199px;height:170px;background:var(--blue)"></div>
  <div class="abs" style="left:331px;top:1983px;width:162px;height:154px;border:2px solid var(--navy)"></div>
  <svg class="abs" style="left:33px;top:2098px" width="70" height="70" viewBox="0 0 70 70"><g fill="var(--navy)">
    <circle cx="2" cy="2" r="1"/><circle cx="2" cy="10" r="1"/><circle cx="2" cy="18" r="1"/><circle cx="2" cy="26" r="1"/><circle cx="2" cy="34" r="1"/><circle cx="2" cy="42" r="1"/><circle cx="2" cy="50" r="1"/><circle cx="2" cy="58" r="1"/><circle cx="2" cy="66" r="1"/>
    <circle cx="10" cy="2" r="1"/><circle cx="10" cy="10" r="1"/><circle cx="10" cy="18" r="1"/><circle cx="10" cy="26" r="1"/><circle cx="10" cy="34" r="1"/><circle cx="10" cy="42" r="1"/><circle cx="10" cy="50" r="1"/><circle cx="10" cy="58" r="1"/><circle cx="10" cy="66" r="1"/>
    <circle cx="18" cy="58" r="1"/><circle cx="26" cy="58" r="1"/><circle cx="34" cy="58" r="1"/><circle cx="42" cy="58" r="1"/><circle cx="50" cy="58" r="1"/><circle cx="58" cy="58" r="1"/><circle cx="66" cy="58" r="1"/>
    <circle cx="18" cy="66" r="1"/><circle cx="26" cy="66" r="1"/><circle cx="34" cy="66" r="1"/><circle cx="42" cy="66" r="1"/><circle cx="50" cy="66" r="1"/><circle cx="58" cy="66" r="1"/><circle cx="66" cy="66" r="1"/></g></svg>
  <div class="abs" style="left:60px;top:2020px;width:126px;text-align:right;color:#fff">
    <div style="font-size:6.8px;font-weight:700">CONTACT US</div>
    <div class="h-font" style="font-size:17px;line-height:19px;margin-top:6px"><b>Let's Do<br>Good</b><br>Together!</div>
  </div>
  <div class="abs" style="left:207px;top:1998px;width:277px;height:192px;background:#fff;box-shadow:0 3px 12px rgba(0,0,0,.12)"></div>
  <h3 class="abs h-font" style="left:229px;top:2015px;font-size:11px;color:var(--navy);font-weight:400"><b style="font-weight:700">Send Us</b> A Message</h3>
  <div class="field" style="left:231px;top:2046px"><b>Your Name</b><span>John Smith</span></div>
  <div class="field" style="left:354px;top:2046px"><b>Company</b><span>Lorem ipsum dolor sit amet</span></div>
  <div class="field" style="left:231px;top:2087px"><b>Email Address</b><span>John Smith@gmail.com</span></div>
  <div class="field" style="left:354px;top:2087px"><b>Phone</b><span>01122-123-456-789</span></div>
  <div class="field" style="left:231px;top:2128px;width:196px"><b>Message</b><span>Hi, do you have a moment to talk abo...|</span></div>
  <div class="abs" style="left:429px;top:2142px;width:28px;height:28px;border-radius:50%;background:var(--blue);display:flex;align-items:center;justify-content:center"><svg width="11" height="11" viewBox="0 0 11 11"><path d="M10 1 1 5 4 6 5 10Z" fill="#fff"/></svg></div>

  <svg class="abs" style="left:0;top:2218px" width="534" height="217" viewBox="0 0 534 217">
    <path d="M0 30 C120 50 250 25 360 15 C440 8 500 15 534 30 L534 217 0 217Z" fill="var(--navy)"/>
    <path d="M0 18 C120 42 250 12 360 4 C440 -1 500 8 534 22 L534 26 C500 12 440 4 360 8 C250 16 120 46 0 24Z" fill="var(--blue)"/>
    <path d="M0 40 C120 58 250 35 360 26 C250 42 120 64 0 46Z" fill="#fff"/>
  </svg>
  <div class="abs foot" style="left:49px;top:2304px;width:120px"><h6>Contact Us</h6>
    <div class="ci"><i style="border-radius:50%"></i><span>Lorem ipsum dolor sit consectetur adipiscing elit</span></div>
    <div class="ci"><i></i><span>info@zerovan.com</span></div>
    <div class="ci"><i></i><span>555-010-0100</span></div>
    <div class="ci"><i></i><span>+1 (555) 014 - 2290</span></div>
  </div>
  <div class="abs foot" style="left:192px;top:2304px"><h6>Links</h6><ul><li>Home</li><li>Services</li><li>Products</li><li>About Us</li><li>Blog</li></ul></div>
  <div class="abs foot" style="left:238px;top:2323px"><ul><li>Terms &amp; Condition</li><li>Privacy Policy</li><li>Support</li><li>Site Map</li><li>Contact Us</li></ul></div>
  <div class="abs foot" style="left:316px;top:2304px;width:175px"><h6>Subscribe for Updates</h6></div>
  <div class="abs" style="left:318px;top:2325px;width:105px;height:18px;border-radius:9px;background:#fff;font-size:5px;color:#999;padding:6px 0 0 10px">Email Address</div>
  <div class="abs" style="left:429px;top:2325px;width:55px;height:18px;border-radius:9px;background:var(--blue);color:#fff;font-size:6.5px;font-weight:700;display:flex;align-items:center;justify-content:center">SUBMIT</div>
  <div class="abs foot" style="left:318px;top:2356px;font-size:5.5px;display:flex;gap:4px;align-items:center"><span style="width:5px;height:5px;border:1px solid #fff;display:inline-block"></span>Yes, Please Contact me.</div>
  <div class="abs" style="left:318px;top:2374px;width:13px;height:13px;border-radius:50%;border:1px solid #fff"></div>
  <div class="abs" style="left:336px;top:2374px;width:13px;height:13px;border-radius:50%;border:1px solid #fff"></div>
  <div class="abs" style="left:354px;top:2374px;width:13px;height:13px;border-radius:50%;border:1px solid #fff"></div>
  <div class="abs" style="left:0;top:2415px;width:534px;text-align:center;color:#fff;font-size:5.5px">© 2024 Zerovan Medical | All Rights Reserved</div>
</main>

<section class="loader" aria-label="Loading screen"><span class="sq"></span><b>Zerovan</b></section>

</div>
</body>
</html>
```